Zelmiroo Pop Up design for zelmiroo.com website to collect customer data

I want a pop up designed for my site zelmiroo.com. It is for signup to the site itself. I want to give my users some value in order to sign up. I want this to have graphics and to collect their full name, email address, country they are from. It must say Sign up today and receive all these items for free, A $129 Value, 1. Zelmiroo Custom Travel tools on Web App, The Ebook Packing Light for Long Journeys, and the Golden Route Planner Sheets!

I want this to look exciting so people actually sign up.
I want to be able to put this on facebook and add to my wordpress website.
I want it to match my current website
I currently use ninja forms on my site

Once designed this also needs to be coded for my site.
You can get my color scheme right on the site. I want this to pop

thanks

Industry/Entity Type

Travel

Font styles to use
Serif
Sans Serif

Colors
33a6d7
9bcb3c
ffffff

Requirements
Must have
• A graphic of the ebook, an arrow rounded or something bringing attention to the free items. A sign up point asking for first name, last name, email. I use ninja forms and mailchimp. this will be a pop up within all of my blogs and every page of my site, also country

```html
<!DOCTYPE html>
<html lang="en">
<head>
<meta charset="utf-8">
<title>Zelmiroo Sign Up Pop Up</title>
<link href="https://fonts.googleapis.com/css2?family=Roboto:wght@400;500;700;900&display=swap" rel="stylesheet">
<style>
:root{
  --blue:#1596dc;
  --brand-blue:#33a6d7;
  --green:#9bcb3c;
  --white:#ffffff;
  --ink:#222222;
  --muted:#bdbdbd;
  --nav:#9fb6c4;
}
*{box-sizing:border-box;margin:0;padding:0}
html,body{width:1200px;height:1200px;overflow:hidden;background:var(--white);font-family:'Roboto',sans-serif}
.canvas{position:relative;width:1200px;height:1200px;overflow:hidden}

/* Background site page, faded behind the pop up */
.site{position:absolute;inset:0;opacity:.28}
.site-header{position:absolute;left:0;top:0;width:1200px;height:118px;background:var(--white)}
.hamburger{position:absolute;left:133px;top:48px;width:26px}
.hamburger span{display:block;height:3px;background:#666;margin-bottom:5px}
.brand{position:absolute;left:190px;top:38px;display:flex;align-items:center;gap:10px}
.brand-dot{width:22px;height:22px;border-radius:50%;background:var(--brand-blue)}
.brand-name{font-size:40px;font-weight:700;color:var(--brand-blue)}
.social{position:absolute;left:813px;top:26px;display:flex;gap:6px}
.social span{width:32px;height:32px;border-radius:50%;background:var(--green)}
.nav{position:absolute;right:128px;top:70px;text-align:right;font-size:12.5px;font-weight:500;color:var(--nav);line-height:19px;word-spacing:6px}
.hero{position:absolute;left:0;top:118px;width:1200px;height:626px;background:linear-gradient(180deg,#8fa9bd 0%,#a9b6b9 40%,#9a8d72 75%,#7d6c53 100%)}
.finder{position:absolute;left:120px;top:177px;width:956px;height:110px;background:rgba(190,225,245,.9)}
.finder-title{position:absolute;left:18px;top:14px;color:var(--white);font-size:24px;font-weight:700}
.finder-input{position:absolute;left:18px;top:54px;width:200px;height:38px;background:var(--white)}
.finder-btn{position:absolute;right:28px;top:54px;width:60px;height:38px;background:var(--green)}
.tile{position:absolute;width:80px;height:124px;border:1px solid rgba(255,255,255,.8);color:var(--white);font-size:13px;font-weight:500}
.tile span{position:absolute;left:38px;top:82px}
.tile-r span{left:auto;right:22px}
.dots{position:absolute;left:550px;top:722px;display:flex;gap:9px}
.dots span{width:11px;height:11px;border-radius:50%;background:var(--white)}
.ad{position:absolute;left:294px;top:762px;width:609px;height:74px;background:#fff6d6}
.ad-brand{position:absolute;left:22px;top:24px;font-size:19px;font-weight:700;color:#4a86c5}
.ad-title{position:absolute;left:240px;top:6px;font-size:36px;font-weight:900;color:#f3c93a}
.ad-sub{position:absolute;left:206px;top:52px;font-size:13px;color:#e0b840}
.ad-btn{position:absolute;right:22px;top:24px;width:80px;height:26px;background:#4a86c5;color:var(--white);font-size:11px;font-weight:700;text-align:center;line-height:26px}
.welcome{position:absolute;left:120px;top:880px;width:310px}
.welcome h2{font-size:32px;font-weight:700;color:#555;line-height:36px}
.welcome h2 em{font-style:normal;font-weight:400;color:var(--brand-blue);display:block;padding-left:12px}
.welcome p{margin-top:30px;font-size:13px;line-height:23.4px;color:#666}
.insure{position:absolute;left:448px;top:886px;width:334px;height:314px;background:#cfe6f2;padding:12px 9px;color:var(--white)}
.insure h3{font-size:19px;font-weight:700;color:#7aa6c7}
.insure h4{margin-top:26px;font-size:20px;font-weight:400;line-height:25px}
.insure label{display:block;margin-top:6px;font-size:9px}
.insure .field{height:33px;background:var(--white);margin-top:6px;color:#aaa;font-size:13px;padding:9px 12px}
.insure .row{display:flex;gap:10px}
.insure .row>div{flex:1}

/* Pop up */
.popup{position:absolute;left:206px;top:200px;width:788px;height:520px;display:flex;box-shadow:0 6px 30px rgba(0,0,0,.25)}
.popup-media{position:relative;width:399px;height:520px;background:var(--white)}
.popup-photo{position:absolute;left:0;top:0;width:399px;height:350px;background:linear-gradient(180deg,#5a6a75 0%,#3f5566 35%,#2b4a62 60%,rgba(120,150,170,.5) 85%,rgba(255,255,255,0) 100%)}
.perks{position:absolute;left:20px;top:333px;width:360px;display:flex;justify-content:space-between}
.perk{width:120px;text-align:center}
.perk-icon{width:88px;height:88px;border:2px solid var(--blue);border-radius:50%;background:var(--white);margin:0 auto;display:flex;align-items:center;justify-content:center}
.perk-label{margin-top:17px;font-size:11.5px;font-weight:500;line-height:14.4px;color:var(--ink)}
.popup-form{position:relative;width:389px;height:520px;background:var(--blue)}
.popup-title{position:absolute;left:35px;top:96px;color:var(--white);font-size:22px;font-weight:700;line-height:32px;text-transform:uppercase}
.popup-title .free{color:var(--green)}
.input{position:absolute;left:35px;width:319px;height:37px;background:var(--white);font-size:14px;color:var(--muted);padding:10px 9px}
.signup-btn{position:absolute;left:35px;top:452px;width:319px;height:37px;background:var(--green);color:var(--white);font-size:16px;text-align:center;line-height:37px;text-transform:uppercase}
</style>
</head>
<body>
<div class="canvas">

  <div class="site" aria-hidden="true">
    <header class="site-header">
      <div class="hamburger"><span></span><span></span><span></span></div>
      <div class="brand"><span class="brand-dot"></span><span class="brand-name">Zelmiroo</span></div>
      <div class="social"><span></span><span></span><span></span><span></span><span></span><span></span><span></span></div>
      <nav class="nav">SIGN IN BLOG TRAVEL INSURANCE FAVORITES MY ITINERARY TRAVEL PLANS<br>SHOP FLIGHTS HOTELS CARS</nav>
    </header>
    <section class="hero" role="img" aria-label="Hiker looking over a mountain valley">
      <div class="finder">
        <div class="finder-title">FIND AN ADVENTURE</div>
        <div class="finder-input"></div>
        <div class="finder-btn"></div>
      </div>
      <div class="tile" style="left:128px;top:237px"><span>Unique</span></div>
      <div class="tile" style="left:128px;top:371px"><span>Hiking</span></div>
      <div class="tile tile-r" style="left:988px;top:237px"><span>Watersports</span></div>
      <div class="tile tile-r" style="left:988px;top:371px"><span>More</span></div>
    </section>
    <div class="dots"><span></span><span></span><span></span><span></span><span></span><span></span></div>
    <div class="ad">
      <div class="ad-brand">Voyalta.ca</div>
      <div class="ad-title">Top Deals</div>
      <div class="ad-sub">Save now on amazing getaways</div>
      <div class="ad-btn">See Deals</div>
    </div>
    <div class="welcome">
      <h2>Welcome to <em>Zelmiroo</em></h2>
      <p>Your online source for the rarest tours in the world! Join our community to enjoy the benefits of custom tour creation, print your tour details or save to your account for your step by step itinerary. Choose reviewed tours with safety rankings and our Zelmiroo recommended companies with rare tours. Help us grow our online community by recommending interesting adventures your have found along your travels!</p>
    </div>
    <div class="insure">
      <h3>Wander Shield</h3>
      <h4>Travel Insurance. Simple &amp; Flexible.</h4>
      <label>Which countries or regions are you traveling to?</label>
      <div class="field">e.g. Thailand, Vietnam</div>
      <label>What's your country of residence?</label>
      <div class="field">e.g. United States (USA)</div>
      <div class="row">
        <div><label>Start date</label><div class="field">5th Apr 18</div></div>
        <div><label>End date</label><div class="field">11th Apr 18</div></div>
      </div>
      <label>Enter Traveler's Age</label>
    </div>
  </div>

  <div class="popup" role="dialog" aria-label="Sign up">
    <div class="popup-media">
      <div class="popup-photo" role="img" aria-label="Boats on a canal lined with old city buildings"></div>
      <div class="perks">
        <div class="perk">
          <div class="perk-icon">
            <svg width="44" height="48" viewBox="0 0 44 48" fill="none" stroke="#1596dc" stroke-width="2">
              <rect x="3" y="2" width="38" height="26" rx="1"/>
              <rect x="6" y="5" width="32" height="17" fill="#1596dc" stroke="none"/>
              <line x1="18" y1="28" x2="18" y2="33"/><line x1="26" y1="28" x2="26" y2="33"/>
              <rect x="7" y="34" width="30" height="10" rx="2"/>
              <line x1="11" y1="39" x2="33" y2="39" stroke-dasharray="2 2"/>
            </svg>
          </div>
          <div class="perk-label">Zelmiroo<br>Custom Travel<br>tools on Web App</div>
        </div>
        <div class="perk">
          <div class="perk-icon">
            <svg width="36" height="52" viewBox="0 0 36 52" fill="none" stroke="#1596dc" stroke-width="2">
              <rect x="2" y="2" width="32" height="44"/>
              <rect x="3" y="14" width="22" height="10" fill="#1596dc" stroke="none"/>
              <line x1="25" y1="2" x2="25" y2="46"/>
              <path d="M6 46 v5 l3 -2 l3 2 v-5"/>
            </svg>
          </div>
          <div class="perk-label">The Ebook - Packing<br>Light for Long<br>Journeys</div>
        </div>
        <div class="perk">
          <div class="perk-icon">
            <svg width="40" height="56" viewBox="0 0 40 56" fill="none" stroke="#1596dc" stroke-width="2">
              <rect x="2" y="2" width="36" height="52"/>
              <path d="M8 14 l3 3 l5 -6"/><line x1="20" y1="14" x2="32" y2="14"/>
              <rect x="8" y="24" width="7" height="7"/><line x1="20" y1="28" x2="32" y2="28"/>
              <rect x="8" y="38" width="7" height="7"/><line x1="20" y1="42" x2="32" y2="42"/>
            </svg>
          </div>
          <div class="perk-label">The Golden<br>Route Planner<br>Sheets!</div>
        </div>
      </div>
    </div>
    <form class="popup-form">
      <h1 class="popup-title">Sign up today<br>and receive all this<br>worth $129 <span class="free">for free</span></h1>
      <div class="input" style="top:272px">Full name</div>
      <div class="input" style="top:322px">Email</div>
      <div class="input" style="top:374px">Country</div>
      <div class="signup-btn">Sign up now</div>
    </form>
  </div>

</div>
</body>
</html>
```